Real Estate Flyer (Brenton Property)

We need a color CMYK high resolution, print quality horizontal real estate property flyer designed in the sizes of 10" wide and 6.7425" tall and another one in 11" wide and 8.5" tall.
Ad should be professionally looking to U.S. standards. It should be sleek, modern yet classy.
We uploaded in Briefs logo files, agent photo, 2 photos of the property (Must use both) and a sample of a flyer for Vayle Morrow Luxury Residence. We like how the overlay atop the first photo in the Vayle Morrow flyer with the company logo in the overlay. We'd like to incorporate that with our logo, the background color of the overlay should match that of our logo. DON'T CHANGE LOGO COLORS. Only use two colors in ad (exact logo blue color and white). The text in the overlay must be "FOR SALE - Potential Income Producing Commercial Office Building". Other details that should be prominent underneath are "42 Brenton Dr., Schaumburg, IL 60174 - Asking Price: $650,000".
Add "Residential & Commercial" under our company logo in italic font.
Add in flyer: "Located seconds away from the Kettering Rd. & Palden Rd. Intersection"
Add in flyer:
- Completely vacant
- 10,000 sq. ft. building
- 55 Car Parking
- 1.38 acre lot
- Over 20 offices and 5 bathrooms.
- Lease out individual office spaces for great monthly cash flow
Put agent's photo and following details professionally displayed:
Dev Marlo
Managing Broker
847-555-0148
dev.marlo@qtnhomes-example.com
Add from Briefs fair housing logo and PLX logo near agent's information. Logos should be small but yet visible to understand text.
Add at bottom of the ad with separation near agent details:
Looking to Buy or Sell?
I’m your one-stop, full service licensed real estate broker.
I deal with all types of real estate properties: Homes, Condos, Townhomes, Multi-Unit Apartment Buildings and Commercial Spaces.
Let My Experience Guide You Through Every Step of the Process!
Fine print:
©2018 QTN Homes, Inc. All Rights Reserved.

```html
<!DOCTYPE html>
<html lang="en">
<head>
<meta charset="utf-8">
<title>Brenton Property – For Sale Flyer</title>
<link rel="stylesheet" href="https://fonts.googleapis.com/css2?family=Lato:ital,wght@0,300;0,400;0,700;1,400&display=swap">
<style>
  :root {
    --brand-blue: #0d4ea3;
    --white: #ffffff;
    --badge-dark: #111111;
  }
  * { margin: 0; padding: 0; box-sizing: border-box; }
  html, body { width: 1200px; height: 1000px; overflow: hidden; background: var(--white); }
  body { font-family: "Lato", Arial, sans-serif; color: var(--brand-blue); }
  .flyer { position: relative; width: 1200px; height: 1000px; background: var(--white); }

  .photo { position: absolute; }
  .photo--front {
    left: 0; top: 40px; width: 605px; height: 348px;
    background: linear-gradient(180deg, #b9c6d4 0%, #e2c9a6 35%, #d9d2c4 60%, #5b5f52 85%, #3c3f42 100%);
  }
  .photo--lot {
    left: 598px; top: 610px; width: 602px; height: 347px;
    background: linear-gradient(180deg, #8a6a55 0%, #cfc3b0 35%, #b8b2a6 55%, #34383d 75%, #26292d 100%);
  }

  .highlights { position: absolute; left: 641px; top: 101px; width: 470px; font-size: 21px; line-height: 27px; }
  .highlights__location { margin-bottom: 19px; }
  .highlights__list { list-style: none; }
  .highlights__list li::before { content: "• "; }

  .banner {
    position: absolute; left: 0; top: 388px; width: 1200px; height: 222px;
    background: var(--brand-blue); color: var(--white);
  }
  .brand { position: absolute; left: 50px; top: 0; width: 266px; height: 222px; text-align: center; }
  .brand__name {
    position: absolute; left: 0; right: 0; top: 98px;
    display: flex; align-items: center; justify-content: center; gap: 12px;
    font-size: 40px; font-weight: 700; letter-spacing: 1px; line-height: 1; white-space: nowrap;
  }
  .brand__mark { width: 20px; height: 20px; background: var(--white); flex: none; }
  .brand__tagline {
    position: absolute; left: 0; right: 0; top: 173px;
    font-style: italic; font-size: 16px; letter-spacing: 0.3px; white-space: nowrap;
  }
  .banner__divider { position: absolute; left: 327px; top: 12px; width: 1px; height: 198px; background: var(--white); }
  .banner__headline { position: absolute; left: 370px; top: 40px; font-size: 42px; font-weight: 400; line-height: 50px; white-space: nowrap; }
  .banner__address { position: absolute; left: 370px; top: 163px; font-size: 21px; font-weight: 300; white-space: nowrap; }

  .agent__photo {
    position: absolute; left: 57px; top: 657px; width: 102px; height: 107px;
    background: linear-gradient(180deg, #cfd3d6 0%, #9aa0a6 55%, #2a2d33 100%);
    border: 1px solid #444;
  }
  .agent__details { position: absolute; left: 165px; top: 676px; font-size: 14px; line-height: 18px; font-style: normal; white-space: nowrap; }

  .badge { position: absolute; }
  .badge--housing { left: 388px; top: 680px; }
  .badge--listing { left: 458px; top: 692px; }

  .pitch { position: absolute; left: 58px; top: 777px; font-size: 12.5px; line-height: 16px; font-weight: 400; white-space: nowrap; }
  .fine-print { position: absolute; left: 58px; top: 873px; font-size: 12.5px; line-height: 16px; font-weight: 400; white-space: nowrap; }
</style>
</head>
<body>
<main class="flyer">
  <div class="photo photo--front" role="img" aria-label="Photo of the two-storey white office building with dormer windows at sunset"></div>

  <section class="highlights">
    <p class="highlights__location">Located seconds away from the Kettering Rd. &amp; Palden Rd. Intersection</p>
    <ul class="highlights__list">
      <li>Completely vacant</li>
      <li>10,000 sq. ft. building</li>
      <li>55 Car Parking</li>
      <li>1.38 acre lot</li>
      <li>Over 20 offices and 5 bathrooms</li>
      <li>Lease out individual office spaces for great monthly cash flow</li>
    </ul>
  </section>

  <section class="banner">
    <div class="brand">
      <div class="brand__name"><span class="brand__mark"></span>QTN HOMES</div>
      <p class="brand__tagline">RESIDENTIAL &amp; COMMERCIAL</p>
    </div>
    <div class="banner__divider"></div>
    <h1 class="banner__headline">FOR SALE - Potential Income Producing<br>Commercial Office Building</h1>
    <p class="banner__address">42 Brenton Dr., Schaumburg, IL 60174 - Asking Price: $650,000</p>
  </section>

  <div class="agent__photo" role="img" aria-label="Portrait of the managing broker"></div>
  <address class="agent__details">
    Dev Marlo<br>Managing Broker<br>847-555-0148<br>dev.marlo@qtnhomes-example.com
  </address>

  <svg class="badge badge--housing" width="62" height="66" viewBox="0 0 62 66" aria-label="Fair housing badge">
    <rect x="0" y="0" width="62" height="66" fill="var(--badge-dark)"/>
  </svg>
  <svg class="badge badge--listing" width="132" height="56" viewBox="0 0 132 56" aria-label="Listing service badge">
    <rect x="0.5" y="0.5" width="131" height="55" fill="#fff" stroke="#222"/>
    <rect x="12" y="8" width="28" height="40" fill="#222"/>
  </svg>

  <section class="pitch">
    <p>Looking to Buy or Sell?</p>
    <p>I’m your one-stop, full service licensed real estate broker.</p>
    <p>I deal with all types of real estate properties: Homes, Condos, Townhomes,<br>Multi-Unit Apartment Buildings and Commercial Spaces.</p>
    <p>Let My Experience Guide You Through Every Step of the Process!</p>
  </section>
  <footer class="fine-print">
    <p>Fine print:</p>
    <p>©2018 QTN Homes, Inc. All Rights Reserved.</p>
  </footer>

  <div class="photo photo--lot" role="img" aria-label="Photo of the office building and its parking lot with parked cars"></div>
</main>
</body>
</html>
```